Optometrist A5 flyer update 2014

We are an optical / optometrist business needing an existing A5 flyer updated. This flyer has been very successful but needs to be renewed.
We are supplying all the original source files including images.
I have included pdf files with annotations on the alteration we would like made.
We are open to suggestions / alterations to the design of the pamphlet.
We are after a modern design appealing to the various ages of our patient base.

```html
<!DOCTYPE html>
<html lang="en">
<head>
<meta charset="UTF-8">
<title>Frequently Asked Questions – Optometrist Flyer</title>
<link href="https://fonts.googleapis.com/css2?family=Source+Sans+3:wght@400;700&display=swap" rel="stylesheet">
<style>
  :root {
    --panel-green: #6db473;
    --icon-green: #3c9f47;
    --text-white: #ffffff;
    --text-soft: #f3f8f2;
    --divider: rgba(255,255,255,0.9);
    --wall-light: #f2f2ef;
    --wall-mid: #dcdcd6;
    --frame-black: #2a2624;
    --frame-gold: #c9a93c;
    --frame-tortoise: #8a6a3e;
    --frame-red: #c8321f;
    --frame-pink: #e6a99a;
  }
  * { margin: 0; padding: 0; box-sizing: border-box; }
  html, body { width: 846px; height: 1200px; overflow: hidden; }
  body { font-family: "Source Sans 3", Arial, sans-serif; background: #fff; }
  .flyer { position: relative; width: 846px; height: 1200px; overflow: hidden; }

  .info-panel {
    position: absolute; left: 0; top: 0; width: 435px; height: 1200px;
    background: var(--panel-green); color: var(--text-white);
  }

  .frame-display {
    position: absolute; left: 435px; top: 0; width: 411px; height: 1200px;
    background:
      linear-gradient(180deg,
        var(--wall-light) 0%,
        rgba(42,38,36,0.35) 9%,
        var(--frame-pink) 11%,
        var(--wall-light) 20%,
        var(--wall-mid) 30%,
        var(--frame-gold) 37%,
        var(--frame-black) 43%,
        var(--wall-light) 52%,
        var(--wall-mid) 60%,
        var(--frame-tortoise) 67%,
        var(--frame-red) 76%,
        var(--wall-light) 86%,
        var(--wall-mid) 100%);
    opacity: 0.85;
  }

  .faq-title {
    position: absolute; left: 22px; top: 40px;
    font-size: 31.5px; font-weight: 700; white-space: nowrap;
  }
  .faq-item { position: absolute; left: 0; width: 435px; }
  .faq-icon { position: absolute; left: 20px; top: 1px; width: 32px; height: 32px; }
  .faq-question {
    margin-left: 65px; width: 360px;
    font-size: 23px; font-weight: 700; line-height: 26px;
    letter-spacing: 0.3px; white-space: nowrap;
  }
  .faq-answer {
    margin: 20px 0 0 67px; width: 338px;
    font-size: 19px; font-weight: 400; line-height: 26px;
    color: var(--text-soft);
  }
  .faq-answer .line { display: block; white-space: nowrap; }
  .faq-answer .line--full { text-align: justify; text-align-last: justify; white-space: normal; }
  .faq-item--sunglasses { top: 126px; }
  .faq-item--refit { top: 371px; }
  .faq-item--health-fund { top: 643px; }

  .divider {
    position: absolute; left: 20px; top: 910px; width: 385px; height: 1px;
    background: var(--divider);
  }
  .hours { position: absolute; left: 65px; top: 928px; }
  .hours-title { font-size: 25.5px; font-weight: 700; margin-bottom: 12px; white-space: nowrap; }
  .hours-list { list-style: none; font-size: 19px; font-weight: 400; color: var(--text-soft); }
  .hours-list li { height: 33.5px; line-height: 26px; white-space: nowrap; }
</style>
</head>
<body>
<div class="flyer">
  <section class="info-panel">
    <h1 class="faq-title">Frequently Asked Questions</h1>

    <article class="faq-item faq-item--sunglasses">
      <svg class="faq-icon" viewBox="0 0 32 32" aria-hidden="true">
        <circle cx="16" cy="16" r="15" fill="var(--icon-green)" stroke="#fff" stroke-width="1.5"/>
        <path d="M11 9 L21 16 L11 23" fill="none" stroke="#fff" stroke-width="3"/>
      </svg>
      <h2 class="faq-question">Can i have fashion sunglasses<br>made to my prescription?</h2>
      <p class="faq-answer">
        <span class="line line--full">Yes. It does depend on the sunglasses</span>
        <span class="line">and your prescription.</span>
        <span class="line line--full">We offer a range of sunglasses that can</span>
        <span class="line">be fitted with prescription lenses.</span>
      </p>
    </article>

    <article class="faq-item faq-item--refit">
      <svg class="faq-icon" viewBox="0 0 32 32" aria-hidden="true">
        <circle cx="16" cy="16" r="15" fill="var(--icon-green)" stroke="#fff" stroke-width="1.5"/>
        <path d="M11 9 L21 16 L11 23" fill="none" stroke="#fff" stroke-width="3"/>
      </svg>
      <h2 class="faq-question">If I want new prescription lenses<br>fitted to my existing pair of<br>glasses, do I have to go without<br>them for a week?</h2>
      <p class="faq-answer">
        <span class="line line--full">No. We can usually fit new lenses to your</span>
        <span class="line line--full">own frame onsite. You only need to be</span>
        <span class="line">without your glasses for a few hours.</span>
      </p>
    </article>

    <article class="faq-item faq-item--health-fund">
      <svg class="faq-icon" viewBox="0 0 32 32" aria-hidden="true">
        <circle cx="16" cy="16" r="15" fill="var(--icon-green)" stroke="#fff" stroke-width="1.5"/>
        <path d="M11 9 L21 16 L11 23" fill="none" stroke="#fff" stroke-width="3"/>
      </svg>
      <h2 class="faq-question">Do I have to purchase my<br>spectacles where my private<br>health fund directs ?</h2>
      <p class="faq-answer">
        <span class="line line--full">No. It is your decision where to have your</span>
        <span class="line">eyes tested and where to purchase your</span>
        <span class="line line--full">spectacles or contact lenses. We can</span>
        <span class="line line--full">direct bill your private health fund with</span>
        <span class="line">the ClaimPoint system.</span>
      </p>
    </article>

    <div class="divider"></div>

    <section class="hours">
      <h2 class="hours-title">Opening Hours</h2>
      <ul class="hours-list">
        <li>Monday 9.00am - 5.30pm</li>
        <li>Tuesday 9.00am - 6.30pm</li>
        <li>Wednesday 9.00am - 5.30pm</li>
        <li>Thursday 9.00am to 6.30pm</li>
        <li>Friday 9.00am -&nbsp; 5.30pm</li>
        <li>Saturday 9.00am- 1.00pm</li>
      </ul>
    </section>
  </section>

  <div class="frame-display" role="img" aria-label="Photograph of black, gold, tortoiseshell and red spectacle frames displayed on a white wall rack"></div>
</div>
</body>
</html>
```